ashby paving works

Needs to have phone number 0412885107 and email marklowry@pavemail.com.au.
ABN 27613048852
name mark lowry

For all your concreting solutions
Excavation
Exposed & colour concrete
House & shed slabs
Driveways
Landing & steps

Contact Information for Business Card

ph 0412885107
email marklowry@pavemail.com.au.
ABN 27613048852
name mark lowry

```html
<!DOCTYPE html>
<html lang="en">
<head>
<meta charset="utf-8">
<title>Ashby Paving Works — Business Card</title>
<link rel="stylesheet" href="https://fonts.googleapis.com/css2?family=Quicksand:wght@500;600;700&display=swap">
<style>
  :root {
    --backdrop: #e9e6e2;
    --card-white: #f3f3f3;
    --card-shade: #dcdcdc;
    --brand-orange: #ef6b24;
    --brand-orange-light: #f38447;
    --brand-orange-deep: #d95a17;
    --slate: #5f5f5f;
    --ink: #4a4a4a;
    --white: #ffffff;
  }
  * { box-sizing: border-box; margin: 0; padding: 0; }
  html, body {
    width: 1200px; height: 960px; overflow: hidden;
    background: var(--backdrop);
    font-family: "Quicksand", "Helvetica Neue", Arial, sans-serif;
  }
  .card {
    position: absolute; width: 600px; height: 342px; overflow: hidden;
    box-shadow: 0 2px 6px rgba(0,0,0,.18);
  }
  /* Front */
  .card-front {
    left: 302px; top: 127px;
    background: linear-gradient(120deg, var(--card-white) 0%, #fafafa 45%, var(--card-shade) 100%);
  }
  .card-front .corners { position: absolute; inset: 0; }
  .brand-square {
    position: absolute; left: 385px; top: 203px; width: 0; height: 0;
  }
  .brand-mark {
    position: absolute; left: 88px; top: 76px; width: 62px; height: 62px;
    background: var(--brand-orange);
  }
  .brand-divider {
    position: absolute; left: 186px; top: 63px; width: 2px; height: 105px;
    background: var(--brand-orange);
  }
  .brand-block {
    position: absolute; left: 196px; top: 84px; width: 262px; text-align: center;
  }
  .brand-name {
    font-weight: 700; font-size: 23px; letter-spacing: .2px;
    color: var(--brand-orange); line-height: 1; white-space: nowrap;
  }
  .brand-sub {
    display: flex; align-items: center; gap: 8px; margin-top: 4px;
    font-weight: 600; font-size: 17px; letter-spacing: 2.5px; color: var(--slate);
    line-height: 1;
  }
  .brand-sub::before, .brand-sub::after {
    content: ""; flex: 1; height: 2px; background: var(--slate);
  }
  .brand-phone {
    margin-top: 3px; font-weight: 600; font-size: 17px; letter-spacing: 2px;
    color: var(--brand-orange); line-height: 1;
  }
  .contact { position: absolute; left: 68px; top: 234px; }
  .contact-name {
    font-weight: 700; font-size: 23px; color: var(--brand-orange); line-height: 1;
  }
  .contact-line {
    font-weight: 500; font-size: 14.5px; color: var(--ink); line-height: 19px;
  }
  .contact-name + .contact-line { margin-top: 6px; }

  /* Back */
  .card-back {
    left: 299px; top: 500px;
    background: linear-gradient(100deg, var(--brand-orange-light) 0%, var(--brand-orange) 60%, var(--brand-orange-deep) 100%);
  }
  .pattern-field { position: absolute; inset: 0; background: rgba(255,255,255,.04); }
  .back-brand {
    position: absolute; left: 118px; top: 140px; width: 132px;
    font-weight: 700; font-size: 19px; line-height: 21px;
    color: var(--white); text-align: right;
  }
  .services {
    position: absolute; left: 254px; top: 125px; list-style: none;
  }
  .services li {
    font-weight: 500; font-size: 14.5px; line-height: 18px; color: var(--white);
    padding-left: 13px; position: relative;
  }
  .services li::before {
    content: ""; position: absolute; left: 1px; top: 7px; width: 5px; height: 5px;
    background: var(--white); transform: rotate(45deg);
  }
</style>
</head>
<body>
  <section class="card card-front" aria-label="Card front">
    <svg class="corners" width="600" height="342" viewBox="0 0 600 342" aria-hidden="true">
      <polygon points="0,0 108,0 0,108" fill="var(--slate)"/>
      <polygon points="600,235 600,342 493,342" fill="var(--brand-orange-deep)"/>
    </svg>
    <div class="brand-mark" aria-hidden="true"></div>
    <div class="brand-divider" aria-hidden="true"></div>
    <div class="brand-block">
      <div class="brand-name">ASHBY PAVING</div>
      <div class="brand-sub">WORKS</div>
      <div class="brand-phone">0412885107</div>
    </div>
    <div class="contact">
      <div class="contact-name">MARK LOWRY</div>
      <div class="contact-line">marklowry@pavemail.com.au</div>
      <div class="contact-line">ABN 27613048852</div>
    </div>
  </section>

  <section class="card card-back" aria-label="Card back">
    <div class="pattern-field" role="img" aria-label="Faint repeating brand pattern across the card back"></div>
    <div class="back-brand">ASHBY PAVING WORKS</div>
    <ul class="services">
      <li>Excavation</li>
      <li>Exposed &amp; colour concrete</li>
      <li>House &amp; shed slabs</li>
      <li>Driveways</li>
      <li>Landing &amp; steps</li>
    </ul>
  </section>
</body>
</html>
```